Printer Ink Cartridge Box Design

We need a box design for our own private branded printer ink cartridge box.
- Prefer matching colors to our brand logo attached.
- Don't put any particular cartridge photos because we use this box for several different cartridges models. We will put a model sticker on top left corner of the front face.
- You can use either same icons on the template or use your own.
- Don't like too many colors, busy designs.
- Prefer simple, clean and impressive designs.
- Included one competitor's cartridge label sample to show a good concept of matching cartridge design concept.

Target Market(s)

US Tralvik customers

Industry/Entity Type

Printer

Font styles to use
Serif

Requirements
Must have
• Logo attached

```html
<!DOCTYPE html>
<html lang="en">
<head>
<meta charset="utf-8">
<title>Fernquill Ink Cartridge Box Dieline</title>
<link rel="stylesheet" href="https://fonts.googleapis.com/css2?family=Montserrat:wght@500;600;800&family=Noto+Serif&display=swap">
<style>
  :root{
    --paper:#ffffff;
    --cut:#b9b9b9;
    --ink:#1a1a1a;
    --leaf:#6aa84f;
    --violet:#6b5fa8;
    --dim:#666666;
  }
  html,body{margin:0;padding:0;overflow:hidden;background:var(--paper);}
  .canvas{width:1200px;height:1200px;display:block;}
  .cut{fill:none;stroke:var(--cut);stroke-width:1;}
  .panel-title{font-family:"Montserrat",sans-serif;font-weight:600;font-size:13px;fill:var(--ink);}
  .panel-copy{font-family:"Montserrat",sans-serif;font-weight:500;font-size:10.5px;fill:var(--ink);}
  .caution-title{font-family:"Montserrat",sans-serif;font-weight:800;font-size:17px;letter-spacing:2px;fill:var(--ink);}
  .caution-copy{font-family:"Montserrat",sans-serif;font-weight:500;font-size:10.5px;fill:var(--ink);}
  .brand-name{font-family:"Montserrat",sans-serif;font-weight:600;font-size:30px;letter-spacing:1px;fill:var(--violet);}
  .dimension{font-family:"Noto Serif",serif;font-size:13px;fill:var(--dim);letter-spacing:1px;}
  .dim-line{stroke:#999;stroke-width:0.8;}
  .icon-frame{fill:#fff;stroke:var(--ink);stroke-width:1.5;}
  .icon-line{fill:none;stroke:var(--ink);stroke-width:1.6;stroke-linecap:round;}
</style>
</head>
<body>
<svg class="canvas" viewBox="0 0 1400 1400" xmlns="http://www.w3.org/2000/svg">
  <defs>
    <linearGradient id="sideBand" x1="0" y1="0" x2="0" y2="1">
      <stop offset="0" stop-color="#f0f1da"/>
      <stop offset="0.7" stop-color="#e8ecd2"/>
      <stop offset="1" stop-color="#c7d2bd"/>
    </linearGradient>
    <linearGradient id="tuckBand" x1="0" y1="0" x2="1" y2="0">
      <stop offset="0" stop-color="#eff2da"/>
      <stop offset="0.5" stop-color="#f5f6e4"/>
      <stop offset="1" stop-color="#c5cfb4"/>
    </linearGradient>
    <linearGradient id="hangGreen" x1="0" y1="0" x2="1" y2="0">
      <stop offset="0" stop-color="#e6e8c6"/>
      <stop offset="0.7" stop-color="#dfe3bd"/>
      <stop offset="1" stop-color="#bfc8a7"/>
    </linearGradient>
    <linearGradient id="hangBlush" x1="0" y1="0" x2="0" y2="1">
      <stop offset="0" stop-color="#f5d7d2"/>
      <stop offset="1" stop-color="#fcebe7"/>
    </linearGradient>
    <linearGradient id="leafTone" x1="0" y1="0" x2="0" y2="1">
      <stop offset="0" stop-color="#e4efd6"/>
      <stop offset="0.5" stop-color="#b9d195"/>
      <stop offset="1" stop-color="#8a9a7c"/>
    </linearGradient>
    <linearGradient id="blushTone" x1="0" y1="0" x2="0" y2="1">
      <stop offset="0" stop-color="#fbe9e5"/>
      <stop offset="0.6" stop-color="#f2c3b6"/>
      <stop offset="1" stop-color="#d9b0ac"/>
    </linearGradient>
  </defs>

  <!-- left side panel -->
  <g class="side-panel">
    <path class="cut" d="M246 508 V480 L300 412 H360 V490 L369 496"/>
    <rect x="246" y="508" width="123" height="499" fill="url(#sideBand)"/>
    <text class="panel-title" x="261" y="683">Ink Cartridge</text>
    <text class="panel-copy" x="264" y="749">This is a High</text>
    <text class="panel-copy" x="264" y="762">quality product.</text>
    <text class="panel-copy" x="264" y="778">Manufactured</text>
    <text class="panel-copy" x="264" y="791">under guarantee</text>
    <rect x="294" y="947" width="40" height="30" rx="3" fill="#c3cab3"/>
    <path class="cut" d="M246 1007 V1106 H305 V1056 L369 1007"/>
  </g>

  <!-- front panel -->
  <g class="front-panel">
    <path class="cut" d="M369 386 V340 Q369 318 391 318 H688 Q710 318 710 340 V386"/>
    <rect x="369" y="386" width="341" height="122" fill="url(#tuckBand)"/>
    <rect class="cut" x="369" y="508" width="341" height="499"/>
    <rect x="436" y="618" width="208" height="292" fill="url(#leafTone)"
          role="img" aria-label="Layered green leaf illustration with scattered ink droplets"/>
    <circle cx="417" cy="946" r="32" fill="var(--leaf)"/>
    <text class="brand-name" x="464" y="957">FERNQUILL</text>
    <path class="cut" d="M369 1007 V1106 H427 V1055 H652 V1106 H710 V1007"/>
  </g>

  <!-- right side panel -->
  <g class="side-panel">
    <rect x="710" y="508" width="121" height="499" fill="url(#sideBand)"/>
    <text class="panel-title" x="730" y="685">Ink Cartridge</text>
    <text class="panel-copy" x="776" y="746" text-anchor="middle" font-weight="600">Join us!</text>
    <text class="panel-copy" x="776" y="762" text-anchor="middle">Just for beautiful</text>
    <text class="panel-copy" x="776" y="777" text-anchor="middle">world!</text>
    <path class="cut" d="M710 1007 L774 1056 V1106 H831 V1007"/>
  </g>

  <!-- back panel with hang tab -->
  <g class="back-panel">
    <path class="cut" d="M831 237 L853 190 H1150 L1172 237"/>
    <rect x="831" y="237" width="341" height="130" fill="#fff"/>
    <rect x="902" y="237" width="270" height="130" fill="url(#hangGreen)"/>
    <rect x="831" y="367" width="341" height="141" fill="url(#hangBlush)"/>
    <rect class="cut" x="831" y="237" width="341" height="271"/>
    <circle cx="870" cy="323" r="27" fill="#2f8a3c"/>
    <path class="cut" d="M958 326 H984 A17 17 0 0 1 1018 326 H1044 A14 14 0 0 1 1044 354 H958 A14 14 0 0 1 958 326 Z"/>
    <path class="cut" d="M958 390 H1044 A14 14 0 0 1 1044 418 H1018 A17 17 0 0 1 984 418 H958 A14 14 0 0 1 958 390 Z"/>

    <rect class="cut" x="831" y="508" width="341" height="499"/>
    <rect x="1052" y="655" width="120" height="352" fill="url(#blushTone)"
          role="img" aria-label="Soft coral flame illustration with ink droplets"/>

    <text class="caution-title" x="878" y="690">CAUTION!</text>
    <text class="caution-copy" x="870" y="718">• Keep out of reach of children</text>
    <text class="caution-copy" x="870" y="735">• Do not expose cartridge to direct sunlight</text>
    <text class="caution-copy" x="870" y="752">• Do not store the cartridge in high or</text>
    <text class="caution-copy" x="878" y="769">freezing temperature</text>

    <g class="handling-icons">
      <rect class="icon-frame" x="872" y="938" width="36" height="36"/>
      <path class="icon-line" d="M877 956 Q890 938 903 956 Z M890 956 V968 Q890 971 886 970"/>
      <rect class="icon-frame" x="918" y="938" width="36" height="36"/>
      <circle class="icon-line" cx="936" cy="956" r="13"/>
      <path class="icon-line" d="M927 947 L945 965"/>
      <rect class="icon-frame" x="964" y="938" width="36" height="36"/>
      <path class="icon-line" d="M975 944 H989 V954 Q982 962 975 954 Z M982 960 V969 M977 969 H987"/>
      <rect class="icon-frame" x="1010" y="938" width="36" height="36"/>
      <circle class="icon-line" cx="1028" cy="956" r="7"/>
      <path class="icon-line" d="M1028 942 V946 M1028 966 V970 M1014 956 H1018 M1038 956 H1042 M1018 946 L1021 949 M1035 963 L1038 966 M1038 946 L1035 949 M1018 966 L1021 963"/>
      <rect class="icon-frame" x="1056" y="938" width="36" height="36"/>
      <path class="icon-line" d="M1074 944 V962"/>
      <circle cx="1074" cy="966" r="4" fill="var(--ink)"/>
      <path class="icon-line" d="M1060 942 L1088 970"/>
      <path class="icon-line" d="M1112 948 L1120 938 L1128 948 M1136 956 L1132 968 H1120 M1108 958 L1104 966 L1112 970"/>
    </g>
    <path class="cut" d="M831 1007 L891 1056 V1106 H1112 V1056 L1172 1007"/>
  </g>

  <!-- glue flap -->
  <path class="cut" d="M1172 508 H1240 V1021 H1172"/>

  <!-- dimension lines -->
  <g class="dimensions">
    <line class="dim-line" x1="174" y1="508" x2="246" y2="508"/>
    <line class="dim-line" x1="174" y1="1007" x2="246" y2="1007"/>
    <line class="dim-line" x1="198" y1="508" x2="198" y2="720"/>
    <line class="dim-line" x1="198" y1="815" x2="198" y2="1007"/>
    <text class="dimension" transform="translate(203 768) rotate(-90)" text-anchor="middle">110.00 m m</text>

    <line class="dim-line" x1="246" y1="1106" x2="246" y2="1208"/>
    <line class="dim-line" x1="369" y1="1106" x2="369" y2="1208"/>
    <line class="dim-line" x1="710" y1="1106" x2="710" y2="1208"/>
    <line class="dim-line" x1="831" y1="1106" x2="831" y2="1208"/>
    <line class="dim-line" x1="1172" y1="1064" x2="1172" y2="1208"/>

    <line class="dim-line" x1="246" y1="1187" x2="260" y2="1187"/>
    <line class="dim-line" x1="346" y1="1187" x2="492" y2="1187"/>
    <line class="dim-line" x1="570" y1="1187" x2="723" y2="1187"/>
    <line class="dim-line" x1="808" y1="1187" x2="955" y2="1187"/>
    <line class="dim-line" x1="1035" y1="1187" x2="1172" y2="1187"/>
    <text class="dimension" x="303" y="1191" text-anchor="middle">27.00 m m</text>
    <text class="dimension" x="530" y="1191" text-anchor="middle">75.00 mm</text>
    <text class="dimension" x="766" y="1191" text-anchor="middle">27.00 m m</text>
    <text class="dimension" x="995" y="1191" text-anchor="middle">75.00 mm</text>
  </g>
</svg>
</body>
</html>
```